Plumbing & Heating bussiness card design

i do all plumbing and heating work and need a catchy design. keep it simple but eye catching nothing gimicky
i do 24hr call outs
landlord safety checks
all aspects of plumbing and heating
boiler breakdowns
flue sure reg number 648197
i have put up my old card. not to bothered about the front but i have put up the back for the details. mobile number and office are the same and the email has changed to dantapfixer@brevomail.net

Industry/Entity Type

Safety

Contact Information for Business Card

i do 24hr call outs
landlord safety checks
boiler breakdowns

Requirements
Must have
• i do 24hr call outs
• landlord safety checks
• all aspects of plumbing and heating
• boiler breakdowns
• flue sure reg number 648197

```html
<!DOCTYPE html>
<html lang="en">
<head>
<meta charset="utf-8">
<title>B Hartwell Plumbing &amp; Heating – Business Card</title>
<link rel="stylesheet" href="https://fonts.googleapis.com/css2?family=Montserrat:wght@600;700&family=Open+Sans:wght@400;600&display=swap">
<style>
  :root {
    --canvas: #e9e7e3;
    --card-dark: #1f1f1f;
    --card-dark-edge: #2c2c2c;
    --card-light: #ffffff;
    --ink-light: #ffffff;
    --ink-dark: #3a3a3c;
    --brand-red: #c8202f;
    --brand-blue: #2a8fd6;
    --badge-yellow: #f6d400;
    --badge-black: #111111;
  }
  * { box-sizing: border-box; margin: 0; padding: 0; }
  html, body { width: 1200px; height: 900px; overflow: hidden; }
  body {
    background: var(--canvas);
    font-family: "Open Sans", Arial, sans-serif;
    position: relative;
  }
  .card {
    position: absolute;
    left: 280px;
    width: 640px;
    height: 366px;
    border-radius: 4px;
    overflow: hidden;
    box-shadow: 0 6px 18px rgba(0,0,0,0.18);
  }

  /* Back card */
  .card-back {
    top: 52px;
    background: linear-gradient(160deg, var(--card-dark-edge) 0%, var(--card-dark) 55%, #171717 100%);
    color: var(--ink-light);
    display: flex;
    flex-direction: column;
    align-items: center;
    justify-content: center;
    text-align: center;
  }
  .back-brand-name {
    font-family: "Montserrat", Arial, sans-serif;
    font-weight: 700;
    font-size: 48px;
    letter-spacing: 1px;
    line-height: 1;
  }
  .back-brand-trade {
    font-family: "Montserrat", Arial, sans-serif;
    font-weight: 700;
    font-size: 23px;
    letter-spacing: 1px;
    margin-top: 4px;
  }
  .service-list {
    list-style: none;
    margin-top: 26px;
    font-size: 17px;
    line-height: 1.5;
  }
  .service-list .divider { padding: 0 8px; }

  /* Front card */
  .card-front {
    top: 482px;
    background: var(--card-light);
  }
  .corner-mark {
    position: absolute;
    left: 0; top: 0;
  }
  .contact-person {
    position: absolute;
    left: 62px; top: 22px;
  }
  .person-name {
    font-size: 22px;
    font-weight: 600;
    line-height: 1.1;
  }
  .person-name .first { color: var(--brand-blue); }
  .person-name .last { color: var(--brand-red); }
  .person-role {
    font-size: 14px;
    color: var(--brand-red);
  }
  .contact-details {
    position: absolute;
    left: 30px; top: 130px;
    color: var(--brand-red);
    font-size: 15px;
    line-height: 1.35;
  }
  .address { margin-bottom: 12px; }
  .contact-line { display: flex; align-items: center; gap: 7px; }
  .contact-line svg { flex: none; }

  .brand-lockup {
    position: absolute;
    left: 318px; top: 128px;
    width: 300px;
    text-align: center;
    color: var(--ink-dark);
    font-family: "Montserrat", Arial, sans-serif;
    font-weight: 700;
  }
  .lockup-name { font-size: 38px; line-height: 1; letter-spacing: 0.5px; }
  .lockup-trade { font-size: 19px; letter-spacing: 1px; margin-top: 4px; }
  .registration-badge {
    position: absolute;
    left: 440px; top: 232px;
    width: 58px; height: 58px;
    background: var(--badge-yellow);
    border: 5px solid var(--badge-black);
    border-radius: 3px;
  }
  .footer-bands {
    position: absolute;
    left: 0; bottom: 0;
  }
</style>
</head>
<body>

  <section class="card card-back" aria-label="Card back">
    <h1 class="back-brand-name">B HARTWELL</h1>
    <p class="back-brand-trade">PLUMBING &amp; HEATING</p>
    <ul class="service-list">
      <li>I do 24hr call outs<span class="divider">|</span>Landlord safety checks</li>
      <li>All aspects of plumbing and heating</li>
      <li>Boiler breakdowns<span class="divider">|</span>Flue sure reg number 648197</li>
    </ul>
  </section>

  <section class="card card-front" aria-label="Card front">
    <svg class="corner-mark" width="60" height="60" viewBox="0 0 60 60" aria-hidden="true">
      <polygon points="0,0 34,0 0,30" fill="var(--brand-red)"/>
      <polygon points="40,0 54,0 54,46 8,46" fill="var(--brand-blue)"/>
    </svg>

    <div class="contact-person">
      <p class="person-name"><span class="first">Owen</span> <span class="last">Clarke</span></p>
      <p class="person-role">Managing Director</p>
    </div>

    <div class="contact-details">
      <p class="address">12345, Address Goes Here<br>Country Name, 123456</p>
      <p class="contact-line">
        <svg width="12" height="12" viewBox="0 0 12 12" aria-hidden="true"><path d="M2 1h3l1 3-1.5 1a7 7 0 0 0 2.5 2.5L8 6l3 1v3c0 .6-.4 1-1 1A9 9 0 0 1 1 2c0-.6.4-1 1-1z" fill="var(--brand-blue)"/></svg>
        044-123 456 789
      </p>
      <p class="contact-line">
        <svg width="12" height="12" viewBox="0 0 12 12" aria-hidden="true"><rect x="3" y="0.5" width="6" height="11" rx="1.2" fill="var(--brand-blue)"/><rect x="4.2" y="2" width="3.6" height="6" fill="#fff"/></svg>
        044-123 456 789
      </p>
      <p class="contact-line">
        <svg width="12" height="12" viewBox="0 0 12 12" aria-hidden="true"><rect x="0.5" y="2" width="11" height="8" fill="var(--brand-blue)"/><path d="M1 2.5l5 4 5-4" stroke="#fff" stroke-width="1" fill="none"/></svg>
        info@webname.com
      </p>
    </div>

    <div class="brand-lockup">
      <p class="lockup-name">B HARTWELL</p>
      <p class="lockup-trade">PLUMBING &amp; HEATING</p>
    </div>
    <div class="registration-badge" aria-hidden="true"></div>

    <svg class="footer-bands" width="640" height="60" viewBox="0 0 640 60" aria-hidden="true">
      <polygon points="0,0 300,44 292,60 0,60" fill="var(--brand-red)"/>
      <polygon points="306,45 640,45 640,60 298,60" fill="var(--brand-blue)"/>
    </svg>
  </section>

</body>
</html>
```